Business Card Design

educational services
broker of essential services
So I love my A Jar of Plums cards. I love the background.
I like the background on the copper meadow card
I like a little part of each Orchardia card
I want my card to stand out and be professional
I would also like somewhat of a brand
I do not want it to be specific to anything but the world and galaxy
I would like to be able to be used for everything, all encompassing
In spanish Sin quebrantos, not sureother languages but i will do programs for other countries like China, Japan and Korea
Reason: It has been the first week of school and I have not been able to get the feedback I need.
Please change colors to Blue and GOld
Please add ~ over the n in Lidia
Please submit some vertical designs
Please include the world
Please make eagle a watermark
Make sure the Far Horizons doesnt have "preparatory school" under it
I am open to new designs and I will pay more after I chose a designer who seems to get all this stuff in my head!
Reason: Last minute designs were wonderful
Reason: I was out of town and not able to review the wonderful designs posted. I am narrowing the designs down now! I appreciate all the work done thus far.
Hello,
Thank you for all the designs. This is difficult. I have not been able to access them as I was able to last week so please be patient. If you also do web design please send me a message.
Again, thank you. I am down to just a few designs.
Sincerely,
Lidia Varga Pemberton
I have been extremely busy, I should pick a design by the ned of this week. Thank you for your patience
Industry/Entity Type
Business
Contact Information for Business Card
Dr. Lidia Varga Pemberton
www.fhacad.com
(555) 214-8093 US
lidiajovarga@mailnest.com

```html
<!DOCTYPE html>
<html lang="en">
<head>
<meta charset="utf-8">
<title>Far Horizons – Business Card</title>
<link rel="stylesheet" href="https://fonts.googleapis.com/css2?family=Lato:wght@400;700;900&family=Lora:ital,wght@1,700&display=swap">
<style>
  :root {
    --backdrop: #dde6f5;
    --card: #ffffff;
    --maroon: #6a0f3b;
    --gold: #c8b21c;
    --ink: #1d1d1d;
  }
  html, body {
    margin: 0;
    width: 1200px;
    height: 965px;
    overflow: hidden;
    background: var(--backdrop);
  }
  .stage {
    position: relative;
    width: 1200px;
    height: 965px;
  }
  .card {
    position: absolute;
    left: 286px;
    top: 313px;
    width: 630px;
    height: 360px;
    background: var(--card);
    border-radius: 18px;
    overflow: hidden;
  }
  .card__swoosh {
    position: absolute;
    inset: 0;
    width: 630px;
    height: 360px;
  }
  .brand {
    position: absolute;
    left: 30px;
    top: 62px;
    display: flex;
    align-items: center;
    gap: 10px;
  }
  .brand__globe {
    width: 64px;
    height: 64px;
    border-radius: 50%;
    background: var(--maroon);
    flex: none;
  }
  .brand__name {
    font-family: "Lato", sans-serif;
    font-weight: 900;
    font-size: 38px;
    letter-spacing: 1px;
    text-transform: uppercase;
    color: var(--gold);
    line-height: 1;
    white-space: nowrap;
  }
  .holder {
    position: absolute;
    left: 30px;
    top: 202px;
    margin: 0;
    font-family: "Lora", serif;
    font-style: italic;
    font-weight: 700;
    font-size: 20px;
    line-height: 26px;
    color: var(--maroon);
    white-space: nowrap;
  }
  .contacts {
    position: absolute;
    left: 30px;
    top: 274px;
    margin: 0;
    padding: 0;
    list-style: none;
    font-family: "Lato", sans-serif;
    font-size: 15px;
    color: var(--ink);
  }
  .contacts__item {
    display: flex;
    align-items: center;
    gap: 6px;
    height: 18px;
    white-space: nowrap;
  }
  .contacts__icon {
    width: 15px;
    height: 13px;
    fill: var(--maroon);
    flex: none;
  }
</style>
</head>
<body>
<main class="stage">
  <section class="card">
    <svg class="card__swoosh" viewBox="0 0 630 360" aria-hidden="true">
      <path fill="var(--maroon)" d="M535 0 C485 40 462 105 480 150 C505 210 495 285 355 360 L630 360 L630 0 Z"/>
      <path fill="var(--card)" d="M548 0 C508 40 492 100 506 145 C522 195 508 275 372 360 L630 360 L630 0 Z"/>
      <path fill="var(--gold)" d="M560 0 C518 40 505 105 522 150 C540 195 528 272 438 360 L630 360 L630 0 Z"/>
      <path fill="var(--card)" d="M522 140 C542 205 524 285 440 340 C502 290 530 220 522 140 Z"/>
    </svg>

    <div class="brand">
      <span class="brand__globe" role="img" aria-label="World globe"></span>
      <span class="brand__name">Far Horizons</span>
    </div>

    <h1 class="holder">Dr. Lidia Varga Pemberton</h1>

    <ul class="contacts">
      <li class="contacts__item">
        <svg class="contacts__icon" viewBox="0 0 14 12"><path d="M1 3 C1 1 3 0 7 0 C11 0 13 1 13 3 L10 4 L9 2.5 L5 2.5 L4 4 Z M3 5 L11 5 L13 11 L1 11 Z"/></svg>
        (555) 214-8093 US
      </li>
      <li class="contacts__item">
        <svg class="contacts__icon" viewBox="0 0 14 12"><path d="M0 1 L14 1 L14 11 L0 11 Z M1.5 2.5 L7 7 L12.5 2.5 Z" fill-rule="evenodd"/></svg>
        lidiajovarga@mailnest.com
      </li>
      <li class="contacts__item">
        <svg class="contacts__icon" viewBox="0 0 14 12"><path d="M0 0 L14 0 L14 9 L8 9 L8 10.5 L10 10.5 L10 12 L4 12 L4 10.5 L6 10.5 L6 9 L0 9 Z M1.5 1.5 L1.5 7.5 L12.5 7.5 L12.5 1.5 Z" fill-rule="evenodd"/></svg>
        www.fhacad.com
      </li>
    </ul>
  </section>
</main>
</body>
</html>
```